Exceptional Corporate Business Card Design

Hello,

We need an exceptional corporate business card design based on our logo attached. We require:

1. A Variation for letterpress print
2. Standard size of business card 84mm x 55mm (Artwork 88mm x 59mm)
3. Variation for square business card 65mm x 65mm (Artwork 69mm x 69mm)
4. Variation as a one side print
5. Adobe Illustrator files

The company is in the financial industry, dulvant.com

The logo is attached as vector pdf.
regards

```html
<!DOCTYPE html>
<html lang="en">
<head>
<meta charset="utf-8">
<title>Dulvant Business Card</title>
<link href="https://fonts.googleapis.com/css2?family=Tinos:wght@400;700&display=swap" rel="stylesheet">
<style>
  :root {
    --brand-blue: #3b3a92;
    --brand-blue-deep: #2f2e86;
    --brand-blue-light: #4a4a9c;
    --paper: #ffffff;
    --backdrop: #e9e7e3;
    --card-shadow: rgba(40, 30, 20, 0.25);
    --front-split: 250px;
  }
  * { margin: 0; padding: 0; box-sizing: border-box; }
  html, body {
    width: 1200px; height: 914px; overflow: hidden;
    background: var(--backdrop);
    font-family: "Tinos", "Times New Roman", serif;
  }
  .canvas { position: relative; width: 1200px; height: 914px; }

  .card {
    position: absolute;
    width: 540px; height: 354px;
    background: var(--paper);
    box-shadow: 0 6px 18px var(--card-shadow);
    overflow: hidden;
  }
  .card--back { left: 600px; top: 90px; }
  .card--front { left: 60px; top: 470px; }

  .band { position: absolute; left: 0; right: 0; background: var(--brand-blue); }
  .card--back .band--top { top: 0; height: 22px; }
  .card--back .band--top-line { top: 28px; height: 5px; }
  .card--back .band--bottom-line { bottom: 62px; height: 5px; }
  .card--back .band--bottom { bottom: 0; height: 56px; }

  .wordmark {
    position: absolute;
    display: flex; align-items: center; gap: 14px;
    color: var(--brand-blue);
    font-weight: 700;
    letter-spacing: 0.02em;
    white-space: nowrap;
    line-height: 1;
  }
  .wordmark__dot {
    border-radius: 50%;
    background: var(--brand-blue);
    flex: none;
  }
  .card--back .wordmark { left: 0; right: 0; top: 140px; justify-content: center; font-size: 62px; }
  .card--back .wordmark__dot { width: 56px; height: 56px; }

  .card--front .wordmark {
    left: 0; width: var(--front-split); top: 124px;
    justify-content: center; font-size: 33px; gap: 8px;
  }
  .card--front .wordmark__dot { width: 32px; height: 32px; }
  .card--front .band--left-line { top: 248px; right: auto; width: var(--front-split); height: 4px; }
  .card--front .band--left { top: 258px; right: auto; width: var(--front-split); height: 18px; }

  .contact-panel {
    position: absolute; left: var(--front-split); top: 0; right: 0; bottom: 0;
    background: linear-gradient(135deg, var(--brand-blue-light), var(--brand-blue-deep));
    color: var(--paper);
    text-align: center;
  }
  .contact-panel__rule {
    position: absolute; left: 0; right: 0; height: 3px; background: var(--paper);
  }
  .contact-panel__rule--outer { top: 8px; }
  .contact-panel__rule--inner { top: 15px; height: 2px; }

  .contact-panel__name { margin-top: 74px; font-size: 28px; font-weight: 700; line-height: 1.1; }
  .contact-panel__role { font-size: 13px; margin-top: 2px; }
  .contact-panel__details { margin-top: 58px; font-size: 17px; line-height: 1.5; }
</style>
</head>
<body>
<main class="canvas">
  <section class="card card--back" aria-label="Card back">
    <div class="band band--top"></div>
    <div class="band band--top-line"></div>
    <div class="wordmark"><span class="wordmark__dot"></span>DULVANT</div>
    <div class="band band--bottom-line"></div>
    <div class="band band--bottom"></div>
  </section>

  <section class="card card--front" aria-label="Card front">
    <div class="wordmark"><span class="wordmark__dot"></span>DULVANT</div>
    <div class="band band--left-line"></div>
    <div class="band band--left"></div>
    <div class="contact-panel">
      <div class="contact-panel__rule contact-panel__rule--outer"></div>
      <div class="contact-panel__rule contact-panel__rule--inner"></div>
      <p class="contact-panel__name">Daniel Hart</p>
      <p class="contact-panel__role">Project Manager</p>
      <div class="contact-panel__details">
        <p>www.dulvant.com</p>
        <p>office@dulvant.com</p>
        <p>14 Marlow Lane, W2B 7QT,<br>London, England</p>
      </div>
    </div>
  </section>
</main>
</body>
</html>
```